Design the Taste: Help Us Cook Up a Fresh Brochure for Our Wholesale Food Brand!

Overview:
We are looking for a fresh, eye-catching brochure design for our wholesale food company. The brochure can be up to 6 pages and should be visually appealing while clearly presenting our products and services.

Reference:
Please use the attached previous brochure as a guide for layout and style inspiration.

Content Requirements:
The brochure must highlight our key food groups:

Frozen Entrées
Pizzas
Frozen Meals and Party Size
Dry goods and Pasta
Gift Baskets
Delicacies and Sweets
Can do private label
Additional Highlights:

We deliver to our customers.
All products are fresh and locally made in Nashville, TN.

Design Goals:

Modern, appetizing, and professional design

Easy to read and navigate
Should NOT say Brindle's Harbor Market and Eatery but brand colors should resemble our parent company Brindles Harbor Market and Eatery
Strong visual focus on our products
Also mention we can brand with clients information
Incorporate brand colors and style from previous brochure

Phone: (555) 382-0467
https://brindlesbulkandgoods.example/
use any pictures from this site: https://brindlesbulkandgoods.example/

use circle logo for Brindle's Fine Harbor Foods

Outstanding family dining and exquisite imported Italian delights.
Today, you’ll find our locally made dishes in markets, mini-marts, and corner stores across the city, making it easy for your clients to enjoy the taste of Brindle’s at home.

Alongside our prepared foods, we offer a curated selection of imported Italian goods, handcrafted gift baskets made in-house, and our signature marinara sauce, lovingly created from my Tutu’s treasured recipes.

Use only our pictures of pizza, pasta, dry pasta, marina sauce, canolis, frozen entrees, frozen dishes and meat dishes provided in breif and on website. Can also use pictures from our facebook and instra gram
https://www.facebook.com/brindlesbulk
https://www.instagram.com/brindles_bulk/

Target Market(s)

Liquior stores, mini markets, gas stations and mini food places

Industry/Entity Type

Food

Font styles to use
Other font styles liked:
• Valadimir script and new times roman

Colors
59FF00
82FF00
B8FF75
E3FFCB
F4FFEA
EB3D1F
EC4F4E
F09395
F8D3D4
FCEDEE

Requirements
Must have
• Item sectiosn metnioned, logo, phone number and webaddress

```html
<!DOCTYPE html>
<html lang="en">
<head>
<meta charset="utf-8">
<title>What We Offer – Brochure Spread</title>
<link rel="stylesheet" href="https://fonts.googleapis.com/css2?family=EB+Garamond:wght@400;500&family=Great+Vibes&family=Tinos&display=swap">
<style>
  :root {
    --canvas: #e6e6e6;
    --brand-red: #d9202c;
    --brand-green: #2f9a2a;
    --blush: #f8d3d4;
    --blush-light: #fcedee;
    --card: #f7f7f7;
  }
  * { margin: 0; padding: 0; box-sizing: border-box; }
  html, body { width: 1200px; height: 960px; overflow: hidden; background: var(--canvas); }
  .spread {
    position: absolute; left: 25px; top: 67px;
    width: 1150px; height: 825px; display: flex;
    box-shadow: 0 12px 30px rgba(0,0,0,.12);
  }
  .page { position: relative; width: 575px; height: 825px; overflow: hidden; }
  .page-backdrop { position: absolute; inset: 0; }
  .page--left .page-backdrop {
    background:
      radial-gradient(ellipse 70% 35% at 40% 92%, rgba(226,120,80,.55), rgba(226,120,80,0) 70%),
      linear-gradient(180deg, var(--blush-light) 0%, #f7e1e2 20%, #efd3d0 45%, #ecc4b6 68%, #e8ae92 86%, #e39a78 100%);
  }
  .page--right .page-backdrop {
    background:
      radial-gradient(ellipse 80% 30% at 60% 95%, rgba(240,214,130,.7), rgba(240,214,130,0) 70%),
      linear-gradient(180deg, var(--blush-light) 0%, #f6e2e3 18%, #e9dcd8 40%, #ded6cd 60%, #e6dcc0 80%, #eedba0 100%);
  }
  .page--right { border-left: 1px solid rgba(0,0,0,.06); }

  .offer-heading {
    position: absolute; left: 58px; top: 52px;
    font-family: "Tinos", "Times New Roman", serif; font-weight: 400;
    font-size: 33px; color: var(--brand-red); letter-spacing: .3px;
  }
  .heading-rule {
    position: absolute; left: 345px; top: 83px; width: 177px; height: 1.5px;
    background: var(--brand-green);
  }
  .menu-tagline {
    position: absolute; left: 56px; top: 46px;
    font-family: "Great Vibes", cursive; font-size: 34px; color: var(--brand-red);
  }
  .menu-sub {
    position: absolute; left: 56px; top: 97px;
    font-family: "Tinos", "Times New Roman", serif; font-size: 16px; color: var(--brand-green);
  }

  .category-card {
    position: absolute; height: 174px;
    background: linear-gradient(90deg, #fafafa, #efefef 60%, #f7f7f7);
    border-radius: 14px;
    box-shadow: 0 3px 8px rgba(0,0,0,.16);
  }
  .page--left .category-card { left: 60px; width: 462px; }
  .page--right .category-card { left: 57px; width: 453px; }
  .category-title {
    position: absolute; left: 19px; top: 10px;
    font-family: "EB Garamond", serif; font-weight: 500;
    font-size: 35px; color: var(--brand-green); white-space: nowrap;
  }
  .thumb-row { position: absolute; left: 18px; top: 61px; display: flex; gap: 15px; }
  .page--right .thumb-row { gap: 14px; }
  .thumb {
    width: 95px; height: 95px; border-radius: 10px;
    box-shadow: 0 1px 3px rgba(0,0,0,.2);
  }
  .page--right .thumb { width: 93px; height: 93px; }
  .t-red    { background: radial-gradient(circle at 50% 45%, #ef9a74, #d9643e 60%, #e8c7a8); }
  .t-brown  { background: radial-gradient(circle at 50% 45%, #c99a70, #9c6744 60%, #cdb79a); }
  .t-cheese { background: radial-gradient(circle at 50% 45%, #f3c98a, #e58a55 60%, #efd8b8); }
  .t-pack   { background: radial-gradient(circle at 50% 45%, #b89484, #6e5a54 65%, #4a4240); }
  .t-white  { background: radial-gradient(circle at 50% 45%, #f2e6b4, #d2c27e 60%, #a8a27a); }
  .t-pizza  { background: radial-gradient(circle at 50% 45%, #eebf80, #d06a44 60%, #ead7b0); }
  .t-green  { background: radial-gradient(circle at 50% 45%, #e6b08a, #cc5a42 55%, #7f9c5a); }
  .t-table  { background: radial-gradient(circle at 50% 45%, #efe6dc, #d6866a 60%, #ece4da); }
  .t-meat   { background: radial-gradient(circle at 50% 45%, #e0a29a, #b06a5c 60%, #d8c5a8); }
  .t-room   { background: radial-gradient(circle at 50% 45%, #c07a5a, #7a4a3a 60%, #4a3a34); }
  .t-dark   { background: radial-gradient(circle at 50% 45%, #b4a8a4, #7a6e6a 60%, #4e4644); }
  .t-pasta  { background: radial-gradient(circle at 50% 45%, #e3cd90, #b79c5e 60%, #8f7f52); }
  .t-sauce  { background: radial-gradient(circle at 50% 45%, #e0604a, #f1dede 58%, #d24a48); }
  .t-basket { background: radial-gradient(circle at 50% 45%, #d9a86a, #b5523e 60%, #8a5a3a); }
  .t-wicker { background: radial-gradient(circle at 50% 45%, #f3ece2, #dcb57c 60%, #bf9358); }
  .t-cake   { background: radial-gradient(circle at 50% 45%, #9a6a56, #5a3a30 60%, #c8b2a4); }
  .t-oreo   { background: radial-gradient(circle at 50% 45%, #f4f2f0, #8a8484 60%, #e6e2e0); }
  .t-berry  { background: radial-gradient(circle at 50% 45%, #f1e2b8, #a58ac4 60%, #e8d8b0); }
  .t-cannoli{ background: radial-gradient(circle at 50% 45%, #f6efe6, #dc9a62 60%, #f2ebe2); }
</style>
</head>
<body>
<main class="spread">
  <section class="page page--left">
    <div class="page-backdrop" role="img" aria-label="Red and white gingham tablecloth fading into a close-up photo of a cheese pizza"></div>
    <h1 class="offer-heading">WHAT WE OFFER</h1>
    <div class="heading-rule"></div>

    <article class="category-card" style="top:133px">
      <h2 class="category-title">Frozen Entrées</h2>
      <div class="thumb-row">
        <div class="thumb t-red" role="img" aria-label="Baked ziti with melted cheese"></div>
        <div class="thumb t-brown" role="img" aria-label="Meat sauce pasta with parmesan"></div>
        <div class="thumb t-cheese" role="img" aria-label="Cheese-topped manicotti"></div>
        <div class="thumb t-pack" role="img" aria-label="Packaged frozen entrée trays"></div>
      </div>
    </article>

    <article class="category-card" style="top:333px">
      <h2 class="category-title">Pizzas</h2>
      <div class="thumb-row">
        <div class="thumb t-white" role="img" aria-label="White pizza with spinach"></div>
        <div class="thumb t-pizza" role="img" aria-label="Sliced supreme pizza"></div>
        <div class="thumb t-cheese" role="img" aria-label="Cheese pizza slice being served"></div>
        <div class="thumb t-green" role="img" aria-label="Margherita pizza with basil"></div>
      </div>
    </article>

    <article class="category-card" style="top:533px">
      <h2 class="category-title">Frozen Meals and Party Size</h2>
      <div class="thumb-row">
        <div class="thumb t-table" role="img" aria-label="Pasta dinner spread with wine"></div>
        <div class="thumb t-meat" role="img" aria-label="Antipasto party platter"></div>
        <div class="thumb t-room" role="img" aria-label="Restaurant bar interior"></div>
        <div class="thumb t-dark" role="img" aria-label="Dining room with checkered tables"></div>
      </div>
    </article>
  </section>

  <section class="page page--right">
    <div class="page-backdrop" role="img" aria-label="Red and white gingham tablecloth fading into a photo of a breakfast plate with omelette"></div>
    <p class="menu-tagline">Our menu, wherever you want it</p>
    <p class="menu-sub">Don't feel like cooking today? We've got you covered - order now!</p>

    <article class="category-card" style="top:128px">
      <h2 class="category-title">Brindles Brand Pasta</h2>
      <div class="thumb-row">
        <div class="thumb t-pasta" role="img" aria-label="Penne with vegetables"></div>
        <div class="thumb t-cheese" role="img" aria-label="Baked stuffed pasta"></div>
        <div class="thumb t-white" role="img" aria-label="Cheesy baked lasagna"></div>
        <div class="thumb t-sauce" role="img" aria-label="Spaghetti with marinara on gingham"></div>
      </div>
    </article>

    <article class="category-card" style="top:332px">
      <h2 class="category-title">Gift Baskets</h2>
      <div class="thumb-row">
        <div class="thumb t-basket" role="img" aria-label="Gift basket of imported goods"></div>
        <div class="thumb t-wicker" role="img" aria-label="Wrapped wicker gift basket"></div>
        <div class="thumb t-basket" role="img" aria-label="Basket with sauces and pasta"></div>
        <div class="thumb t-sauce" role="img" aria-label="Basket on checkered cloth"></div>
      </div>
    </article>

    <article class="category-card" style="top:534px">
      <h2 class="category-title">Delicacies and Sweets</h2>
      <div class="thumb-row">
        <div class="thumb t-cake" role="img" aria-label="Chocolate layer cake slice"></div>
        <div class="thumb t-oreo" role="img" aria-label="Cookies and cream cheesecake"></div>
        <div class="thumb t-berry" role="img" aria-label="Blueberry cake slice"></div>
        <div class="thumb t-cannoli" role="img" aria-label="Powdered cannoli"></div>
      </div>
    </article>
  </section>
</main>
</body>
</html>
```